Lumen Cove Skincare - Package Design

New Beauty label needing product packaging design. Looking for elegant and stylish design to represent our premium brand.

This project is for 1 label and 1 box design. The winning designer will be assigned another project for the next product in the range. (to be paid as a new project)

This product is for "Dead Sea Mud Mask". Please see the label format and jar attached. Please note there are 2 different jars we are considering (will have a mud inside). Please feel free to choose whichever one suits your design best.

The labels and boxes are to retain the product information, such as size, ingredients etc, but is to be updated to our brand. You can move or display the other information as you wish.

the size of the dead sea mud mask color box is 72*72*85mm (length*width*height)
the size of dead sea mud mask label is 218*58mm (width*height)

Target Market(s)

Women 15 to 65

Requirements
Must have
• Must be elegant and represent our brand which is a premium beauty product.
Should not have
• Dark blue. Dark purple etc. Colours should compliment the logo

```html
<!DOCTYPE html>
<html lang="en">
<head>
<meta charset="utf-8">
<title>Lumen Cove Skincare – Dead Sea Mud Mask Packaging</title>
<link href="https://fonts.googleapis.com/css2?family=Bebas+Neue&family=Lato:wght@300;400;700;900&display=swap" rel="stylesheet">
<style>
  :root{
    --page:#ffffff;
    --slate:#5a6970;
    --slate-deep:#4f5d64;
    --wave-a:#5f6f77;
    --wave-b:#7b8d96;
    --aqua:#7ed4e8;
    --mist:#d3dade;
    --label-edge:#3e4a50;
  }
  *{margin:0;padding:0;box-sizing:border-box}
  html,body{width:1200px;height:1200px;overflow:hidden;background:var(--page)}
  .canvas{position:relative;width:1200px;height:1200px;font-family:"Lato",sans-serif}

  /* Box dieline panels */
  .box{position:absolute;left:220px;top:70px;display:flex}
  .panel{position:relative;width:380px;height:450px;background:var(--slate);overflow:hidden}
  .panel + .panel{border-left:1px solid var(--slate-deep)}
  .waves{position:absolute;left:0;right:0;bottom:0;height:150px;
    background:linear-gradient(180deg,var(--slate) 0%,var(--wave-a) 30%,var(--wave-b) 60%,var(--wave-a) 100%)}

  .directions{position:absolute;left:26px;top:40px;width:328px;color:var(--mist);font-weight:300;font-size:11.5px;line-height:1.32;text-align:justify;z-index:1}
  .directions h3{font-weight:400;font-size:11.5px;letter-spacing:.5px;margin-bottom:14px}
  .directions p{margin-bottom:14px}
  .warning{position:absolute;left:26px;top:318px;color:var(--mist);font-size:11.5px;z-index:1}
  .warning strong{display:block;font-weight:700;margin-bottom:3px}
  .warning span{font-weight:300}

  .brand{display:flex;align-items:center;justify-content:center;gap:8px;color:var(--aqua);font-weight:400;letter-spacing:1px}
  .brand-dot{width:10px;height:10px;border:1.5px solid var(--aqua);border-radius:50%}
  .front .brand{position:absolute;top:78px;left:0;right:0;font-size:17px}
  .title{font-family:"Bebas Neue",sans-serif;color:var(--aqua);text-align:center;letter-spacing:.5px}
  .front .title{position:absolute;top:168px;left:0;right:0;font-size:52px}
  .claims{color:var(--aqua);font-weight:700;text-align:center}
  .front .claims{position:absolute;top:234px;left:0;right:0;font-size:13px}
  .pitch{color:var(--aqua);font-weight:900;text-transform:uppercase;line-height:1.15}
  .front .pitch{position:absolute;top:318px;left:30px;width:240px;font-size:13px;z-index:1}
  .natural{position:absolute;display:flex;flex-direction:column;align-items:center;color:var(--aqua);font-weight:900;line-height:1;z-index:1}
  .natural .ring{border:2px solid var(--aqua);border-radius:50%}
  .front .natural{right:26px;top:300px;font-size:12px}
  .front .natural .ring{width:44px;height:44px;margin-bottom:6px}
  .size{font-family:"Bebas Neue",sans-serif;color:var(--aqua);text-align:center;letter-spacing:.5px;z-index:1}
  .front .size{position:absolute;bottom:22px;left:0;right:0;font-size:22px}

  /* Jar label */
  .label{position:absolute;left:100px;top:620px;width:1000px;height:266px;background:var(--slate);overflow:hidden;border-top:6px solid var(--label-edge)}
  .label .waves{height:120px}
  .label .brand{position:absolute;top:22px;left:0;right:0;font-size:16px}
  .label .title{position:absolute;top:56px;left:0;right:0;font-size:54px}
  .label .claims{position:absolute;top:122px;left:0;right:0;font-size:14px}
  .label .pitch{position:absolute;top:160px;left:330px;width:280px;font-size:10.5px;z-index:1}
  .label .natural{left:640px;top:152px;font-size:10px}
  .label .natural .ring{width:34px;height:34px;margin-bottom:4px}
  .label .size{position:absolute;bottom:18px;left:0;right:0;font-size:18px}
</style>
</head>
<body>
<main class="canvas">
  <section class="box" aria-label="Box panels">
    <article class="panel side">
      <div class="directions">
        <h3>DIRECTIONS</h3>
        <p>Mauris purus. Donec est nunc, ornare non, aliquet non, tempus vel, dolor. Integer sapien nibh, egestas ut, cursus sit amet, faucibus a, sapien. Vestibulum purus purus, elementum ac, luctus ullamcorper, ornare vitae, massa. Nullam posuere sem ut mauris. Nullam velit. Quisque sodales. Donec suscipit suscipit erat. Nam blandit. Praesent congue lorem non dolor. Maecenas vitae erat. Ut ac purus vel purus dapibus gravida.</p>
        <p>Nullam lorem sapien, tempus ac, fringilla at, elementum sed, purus. Duis molestie pede.</p>
      </div>
      <div class="warning"><strong>FOR EXTERNAL USE ONLY</strong><span>Keep out of reach of children</span></div>
      <div class="waves" role="img" aria-label="Brushed wave stripe pattern in slate blue tones"></div>
    </article>
    <article class="panel front">
      <div class="brand"><span class="brand-dot"></span>Lumen Cove Skincare</div>
      <h1 class="title">Dead Sea Mud Mask</h1>
      <p class="claims">Anti-Acne • Deep Skin Cleanser • Pore Reducer</p>
      <p class="pitch">100% natural minieral-infused detoxifier packed with vitamins to promote youthful skin</p>
      <div class="natural"><span class="ring"></span>100%<br>NATURAL</div>
      <p class="size">250 G 8.8 FL.OZ</p>
      <div class="waves" role="img" aria-label="Brushed wave stripe pattern in slate blue tones"></div>
    </article>
  </section>

  <section class="label" aria-label="Jar label">
    <div class="brand"><span class="brand-dot"></span>Lumen Cove Skincare</div>
    <h2 class="title">Dead Sea Mud Mask</h2>
    <p class="claims">Anti-Acne • Deep Skin Cleanser • Pore Reducer</p>
    <p class="pitch">100% natural minieral-infused detoxifier packed with vitamins to promote youthful skin</p>
    <div class="natural"><span class="ring"></span>100%<br>NATURAL</div>
    <p class="size">250 G 8.8 FL.OZ</p>
    <div class="waves" role="img" aria-label="Brushed wave stripe pattern in slate blue tones"></div>
  </section>
</main>
</body>
</html>
```